Team Member Spotlight 'Stats Card' Design for ProfilNet

We are creating a 'Stats Card'-style team member spotlight post for our company's ProfilNet page. The design should be professional yet fun, reflecting our company's approachable and innovative brand. Here’s what we need:

Header featuring:
Name: Reed Calloway
Role: Area Sales Manager - Austin, TX
Photo: Will provide
Quick stats section with bold, modern fonts:
Years in Pain Management: 8 years
Time at OKRA VENT QS: 1 year (by February)
Favorite Quote: “Nothing in the world can take the place of persistence.” – Ambrose Thistlewood
Hobby/Passion: Making music (on Tunevault as Reed Calloway!)
Football Team: Pelham Tech (Herons)

Use vibrant, approachable company branding colors.
Incorporate small themed icons (e.g., music notes, football elements).
Clean, modern layout with clear sections and engaging visuals.
Subtle background details that hint at music and Texas without overpowering the content.

Optimized for ProfilNet dimensions (square or portrait format).
Delivered in editable file formats (Canva) for future use.

Professional but approachable.
Engaging design that will catch attention while staying on-brand.
We will provide the company branding guide, Reed’s photo, and detailed stats. The design should feel cohesive with our brand and stand out on ProfilNet.

Industry/Entity Type

Medical Device / Physicians

Colors

Designer to choose colors to be used in the design.

Requirements
Must have
• Include OKRA VENT QS logo & Company Colors: #a9218f & #011842

```html
<!DOCTYPE html>
<html lang="en">
<head>
<meta charset="utf-8">
<title>Reed Calloway – Team Spotlight</title>
<link href="https://fonts.googleapis.com/css2?family=Roboto+Condensed:wght@500;600;700&display=swap" rel="stylesheet">
<style>
  :root{
    --brand-navy:#011842;
    --indigo:#1c2a7a;
    --royal:#1f4fae;
    --sky:#0a90dc;
    --cyan:#1aa3e8;
    --magenta:#a9218f;
    --magenta-light:#c23aa7;
    --white:#ffffff;
    --faint:rgba(255,255,255,.12);
  }
  *{margin:0;padding:0;box-sizing:border-box}
  html,body{width:964px;height:1200px;overflow:hidden;background:#fff}
  .card{
    position:relative;width:964px;height:1200px;overflow:hidden;
    font-family:"Roboto Condensed","Arial Narrow",sans-serif;color:var(--white);
    background:linear-gradient(115deg,var(--brand-navy) 0%,var(--indigo) 30%,var(--royal) 55%,var(--sky) 85%,var(--cyan) 100%);
  }
  .backdrop{position:absolute;inset:0}
  .box{position:absolute;
    background:linear-gradient(90deg,rgba(10,144,220,.92),rgba(1,24,66,.75));
    border:1.5px solid rgba(255,255,255,.35);border-left:none;border-radius:0 26px 26px 0}
  .brand{left:0;top:16px;width:417px;height:150px;display:flex;align-items:center;justify-content:center}
  .brand-name{font-weight:600;font-size:62px;letter-spacing:1px;line-height:1;color:var(--white)}
  .name-pill{position:absolute;left:135px;top:190px;width:375px;height:100px;background:var(--magenta);
    border-radius:70px 0 0 0;display:flex;align-items:center;justify-content:flex-end;padding-right:8px}
  .name-pill h1{font-weight:700;font-size:54px;letter-spacing:.5px;line-height:1}
  .role-pill{position:absolute;left:135px;top:309px;width:415px;height:110px;
    background:linear-gradient(90deg,var(--sky),var(--royal));border-radius:0 0 0 80px;
    border:1.5px solid rgba(255,255,255,.35);border-left:none;padding:14px 0 0 62px}
  .role-pill p{font-weight:600;font-size:32px;line-height:46px}
  .role-pill p + p{padding-left:8px}
  .portrait{position:absolute;left:540px;top:93px;width:400px;height:400px;border-radius:50%;
    background:radial-gradient(circle at 55% 45%,#c9a38a 0%,#6b4a35 35%,#2a2f4d 70%,#1d2f6e 100%)}
  .stat{padding:20px 0 0 34px;font-weight:600;font-size:32px;line-height:47px}
  .stat-time{top:456px;width:384px;height:118px}
  .stat-years{top:590px;width:469px;height:124px;padding-top:24px}
  .stat-team{top:727px;width:518px;height:130px;padding:26px 0 0 39px}
  .stat-hobby{top:873px;width:620px;height:130px;padding:26px 0 0 39px}
  .team-badge{position:absolute;left:362px;top:752px;width:80px;height:80px;background:var(--faint);border-radius:6px}
  .music-dot{position:absolute;left:512px;top:899px;width:80px;height:80px;border-radius:50%;background:var(--sky)}
  .quote-back{position:absolute;left:24px;top:1031px;width:393px;height:146px;background:var(--magenta);border-radius:36px}
  .quote-label,.quote-author{position:absolute;left:70px;font-weight:600;font-size:32px;line-height:1}
  .quote-label{top:1040px}
  .quote-author{top:1134px}
  .quote-pill{position:absolute;left:44px;top:1080px;width:870px;height:46px;border-radius:23px;
    background:linear-gradient(90deg,var(--sky),var(--royal) 70%,var(--brand-navy));border:1.5px solid rgba(255,255,255,.6);
    display:flex;align-items:center;padding-left:24px;font-weight:600;font-size:32px;white-space:nowrap}
</style>
</head>
<body>
<main class="card">
  <svg class="backdrop" width="964" height="1200" viewBox="0 0 964 1200">
    <defs>
      <g id="dots" fill="#fff">
        <circle cx="0" cy="0" r="2.5"/><circle cx="10" cy="0" r="2.5"/><circle cx="20" cy="0" r="2.5"/><circle cx="30" cy="0" r="2.5"/><circle cx="40" cy="0" r="2.5"/><circle cx="50" cy="0" r="2.5"/>
        <circle cx="0" cy="10" r="2.5"/><circle cx="10" cy="10" r="2.5"/><circle cx="20" cy="10" r="2.5"/><circle cx="30" cy="10" r="2.5"/><circle cx="40" cy="10" r="2.5"/><circle cx="50" cy="10" r="2.5"/>
        <circle cx="0" cy="20" r="2.5"/><circle cx="10" cy="20" r="2.5"/><circle cx="20" cy="20" r="2.5"/><circle cx="30" cy="20" r="2.5"/><circle cx="40" cy="20" r="2.5"/><circle cx="50" cy="20" r="2.5"/>
        <circle cx="0" cy="30" r="2.5"/><circle cx="10" cy="30" r="2.5"/><circle cx="20" cy="30" r="2.5"/><circle cx="30" cy="30" r="2.5"/><circle cx="40" cy="30" r="2.5"/><circle cx="50" cy="30" r="2.5"/>
        <circle cx="0" cy="40" r="2.5"/><circle cx="10" cy="40" r="2.5"/><circle cx="20" cy="40" r="2.5"/><circle cx="30" cy="40" r="2.5"/><circle cx="40" cy="40" r="2.5"/><circle cx="50" cy="40" r="2.5"/>
      </g>
      <g id="note">
        <ellipse cx="0" cy="0" rx="9" ry="7" transform="rotate(-20)"/>
        <rect x="6" y="-38" width="3.5" height="38"/>
        <path d="M9.5 -38 C20 -32 24 -26 18 -16 C20 -24 16 -28 9.5 -30 Z"/>
      </g>
    </defs>

    <path d="M62 0 L62 1200" stroke="var(--faint)" stroke-width="2"/>
    <path d="M250 0 L250 1200" stroke="rgba(255,255,255,.06)" stroke-width="40"/>
    <path d="M60 700 C120 1000 200 1150 220 1200" fill="none" stroke="rgba(255,255,255,.3)" stroke-width="1.5"/>
    <path d="M310 520 C420 900 640 1080 964 1120" fill="none" stroke="rgba(255,255,255,.2)" stroke-width="1.5"/>
    <path d="M400 380 C520 800 720 960 964 980" fill="none" stroke="rgba(255,255,255,.15)" stroke-width="1.5"/>

    <path d="M538 0 H964 V708 C770 706 600 610 552 430 C540 380 538 320 538 260 Z" fill="var(--magenta)"/>
    <path d="M538 160 C538 330 560 450 600 530 C660 640 790 706 964 708" fill="none" stroke="#fff" stroke-width="4"/>
    <circle cx="740" cy="293" r="218" fill="none" stroke="var(--sky)" stroke-width="32"/>
    <circle cx="740" cy="293" r="236" fill="none" stroke="rgba(255,255,255,.55)" stroke-width="3"/>

    <circle cx="505" cy="68" r="50" fill="rgba(10,144,220,.45)"/>
    <circle cx="430" cy="560" r="16" fill="none" stroke="var(--faint)" stroke-width="3"/>
    <circle cx="590" cy="734" r="25" fill="none" stroke="rgba(10,144,220,.6)" stroke-width="3"/>
    <circle cx="830" cy="810" r="65" fill="rgba(255,255,255,.07)"/>
    <circle cx="905" cy="765" r="28" fill="rgba(255,255,255,.07)"/>
    <circle cx="800" cy="745" r="18" fill="rgba(255,255,255,.07)"/>
    <circle cx="790" cy="1055" r="55" fill="rgba(255,255,255,.06)"/>

    <use href="#dots" x="885" y="17"/>
    <use href="#dots" x="885" y="592"/>

    <g fill="rgba(255,255,255,.28)">
      <use href="#note" x="690" y="900"/>
      <use href="#note" x="880" y="930" transform="rotate(8 880 930)"/>
      <use href="#note" x="660" y="1010"/>
    </g>
  </svg>

  <div class="box brand"><span class="brand-name">OKRA VENT QS</span></div>

  <div class="name-pill"><h1>Reed Calloway</h1></div>
  <div class="role-pill"><p>Area Sales Manager</p><p>Austin, TX</p></div>

  <div class="portrait" role="img" aria-label="Portrait photo of Reed Calloway"></div>

  <div class="box stat stat-time">Time at OKRA VENT QS:<br>1 year (by February)</div>
  <div class="box stat stat-years">Years in Pain Management:<br>8 years</div>
  <div class="box stat stat-team">Football Team:<br>Pelham Tech (Herons)</div>
  <div class="team-badge"></div>
  <svg class="football-icon" style="position:absolute;left:452px;top:762px" width="54" height="36" viewBox="0 0 54 36" aria-hidden="true">
    <ellipse cx="27" cy="18" rx="25" ry="15" fill="var(--magenta)" stroke="#fff" stroke-width="2"/>
    <path d="M17 18 H37 M21 14 V22 M25 14 V22 M29 14 V22 M33 14 V22" stroke="#fff" stroke-width="2"/>
  </svg>
  <div class="box stat stat-hobby">Hobby/Passion: Making music<br>(on Tunevault as Reed Calloway!)</div>
  <div class="music-dot"></div>

  <div class="quote-back"></div>
  <p class="quote-label">Favorite Quote:</p>
  <p class="quote-pill">“Nothing in the world can take the place of persistence.”</p>
  <p class="quote-author">Ambrose Thistlewood</p>
</main>
</body>
</html>
```